Tech Savy small Business accountant business card design

We need a business card for a new company based in the cloud. We provide tax, business advisory, accounting, information technology solutions and back office functions to small businesses. We offer fixed fee packages with add on services as you need them. By harnessing technology we simplify small business operational processes providing valuable time and information for small business owners to grow their business. In the logo (quilbrook) we want to be able to see quil and experts. The final design should communicate achieving growth dreams and balance (ie life and $).
Updates
This project has been temporarily placed on hold until I finalize "Tech Savy small Business accountant needs a logo". I invite all designers to submit on this logo project. Once my logo is finalized I will resume this business card contest. Thanks Added Wednesday, March 19, 2014
This project has been temporarily placed on hold until I finalize "Tech Savy small Business accountant logo". I invite all designers to submit on this logo project. Once my logo is finalized I will resume this business card contest. Thanks Added Thursday, March 20, 2014
Target Market(s)
Small Business (Revenue $500,000, more than 3 employees) owners.
Industry/Entity Type
Small Business
Contact Information for Business Card
Marla Henwick (Principal)
Accountant, Tax Agent.
TEL | 0418 663 904
EMAIL | Marla.Henwick@quilbrook-mail.com.au
WEB | www.quilbrook-mail.com.au
Look and feel

```html
<!DOCTYPE html>
<html lang="en">
<head>
<meta charset="utf-8">
<title>Marla Henwick – Business Card</title>
<link rel="stylesheet" href="https://fonts.googleapis.com/css2?family=Cinzel:wght@400;500&family=Courier+Prime:wght@400;700&display=swap">
<style>
  :root {
    --gold: #f5c633;
    --ink-light: #f2f2ee;
    --rule: #8a8a86;
    --bg-centre: #2b2f30;
    --bg-edge: #121112;
  }
  html, body {
    margin: 0;
    padding: 0;
    overflow: hidden;
    background: var(--bg-edge);
  }
  .card {
    position: relative;
    width: 1200px;
    height: 720px;
    overflow: hidden;
    background: radial-gradient(ellipse 60% 65% at 48% 42%, var(--bg-centre) 0%, #1c1d1e 55%, var(--bg-edge) 100%);
  }
  .card__name,
  .card__role {
    position: absolute;
    left: 0;
    width: 100%;
    margin: 0;
    text-align: center;
    color: var(--gold);
    font-family: "Cinzel", serif;
    font-weight: 400;
    white-space: nowrap;
  }
  .card__name {
    top: 98px;
    font-size: 50px;
    letter-spacing: 4px;
  }
  .card__role {
    top: 182px;
    font-size: 44px;
    letter-spacing: 5px;
  }
  .contact {
    position: absolute;
    left: 0;
    height: 60px;
    width: 100%;
    font-family: "Courier Prime", monospace;
    color: var(--ink-light);
  }
  .contact__icon {
    position: absolute;
    top: 50%;
    transform: translateY(-50%);
  }
  .contact__label,
  .contact__value {
    position: absolute;
    top: 50%;
    transform: translateY(-50%);
    white-space: nowrap;
  }
  .contact__rule {
    position: absolute;
    top: 50%;
    width: 1px;
    height: 32px;
    transform: translateY(-50%);
    background: var(--rule);
  }
  .contact--tel { top: 304px; }
  .contact--tel .contact__icon { left: 311px; }
  .contact--tel .contact__label { left: 394px; font-size: 32px; font-weight: 700; letter-spacing: 4px; }
  .contact--tel .contact__rule { left: 494px; }
  .contact--tel .contact__value { left: 536px; font-size: 25px; font-weight: 700; letter-spacing: 3px; }

  .contact--email { top: 434px; }
  .contact--email .contact__icon { left: 311px; }
  .contact--email .contact__label { left: 386px; font-size: 27px; letter-spacing: 3px; }
  .contact--email .contact__rule { left: 499px; }
  .contact--email .contact__value { left: 526px; font-size: 22px; letter-spacing: 3px; }

  .contact--web { top: 600px; }
  .contact--web .contact__icon { left: 311px; }
  .contact--web .contact__label { left: 401px; font-size: 28px; letter-spacing: 7px; }
  .contact--web .contact__rule { left: 502px; }
  .contact--web .contact__value { left: 530px; font-size: 27px; letter-spacing: 6px; }
</style>
</head>
<body>
<main class="card">
  <h1 class="card__name">MARLA HENWICK (PRINCIPAL)</h1>
  <p class="card__role">ACCOUNTANT, TAX AGENT</p>

  <div class="contact contact--tel">
    <svg class="contact__icon" width="54" height="38" viewBox="0 0 54 38" aria-hidden="true">
      <path d="M3 12 C3 4 51 4 51 12 L51 16 L40 16 L40 11 L14 11 L14 16 L3 16 Z" fill="var(--gold)"/>
      <path d="M12 17 L42 17 L50 36 L4 36 Z" fill="var(--gold)"/>
      <circle cx="27" cy="26" r="6.5" fill="var(--bg-edge)"/>
      <circle cx="27" cy="26" r="2.5" fill="var(--gold)"/>
    </svg>
    <span class="contact__label">TEL</span>
    <span class="contact__rule"></span>
    <span class="contact__value">0418 663 904</span>
  </div>

  <div class="contact contact--email">
    <svg class="contact__icon" width="56" height="38" viewBox="0 0 56 38" aria-hidden="true">
      <rect x="1.5" y="1.5" width="53" height="35" fill="none" stroke="var(--gold)" stroke-width="3"/>
      <path d="M2 2 L28 24 L54 2 M2 36 L21 18 M54 36 L35 18" fill="none" stroke="var(--gold)" stroke-width="2.5"/>
    </svg>
    <span class="contact__label">EMAIL</span>
    <span class="contact__rule"></span>
    <span class="contact__value">MARLA.HENWICK@QUILBROOK-MAIL.COM.AU</span>
  </div>

  <div class="contact contact--web">
    <svg class="contact__icon" width="64" height="64" viewBox="0 0 64 64" aria-hidden="true">
      <g fill="none" stroke="var(--gold)" stroke-width="3">
        <circle cx="32" cy="32" r="29"/>
        <ellipse cx="32" cy="32" rx="13" ry="29"/>
        <line x1="32" y1="3" x2="32" y2="61"/>
        <line x1="3" y1="32" x2="61" y2="32"/>
        <path d="M8 17 H56 M8 47 H56"/>
      </g>
    </svg>
    <span class="contact__label">WEB</span>
    <span class="contact__rule"></span>
    <span class="contact__value">WWW.QUILBROOK-MAIL.COM.AU</span>
  </div>
</main>
</body>
</html>
```